Business card design and logo needed - Photographer

I take photos of weddings, rodeos, snowmobiling.
Need a card to hand out to prospective clients.
Industry/Entity Type
Business
Contact Information for Business Card
Marcus Dolven Photography
Requirements
Must have
- Bold
Black or white base.
My website. www.MarcusDolven.example
Should not have
- camera/ lens/ aperture blades

```html
<!DOCTYPE html>
<html lang="en">
<head>
<meta charset="utf-8">
<title>Marcus Dolven Photography – Business Card</title>
<link rel="stylesheet" href="https://fonts.googleapis.com/css2?family=Quicksand:wght@400;500;600&display=swap">
<style>
  :root {
    --page-bg: #e4e6e6;
    --card-base: #1f2829;
    --card-edge: #0e1414;
    --band-light: #2a3738;
    --band-dark: #182021;
    --divider: #121819;
    --text-main: #f2f4f4;
    --text-soft: #c9cfd0;
    --brand-mark: #3f8fe0;
  }
  * { margin: 0; padding: 0; box-sizing: border-box; }
  html, body {
    width: 1200px;
    height: 1000px;
    overflow: hidden;
    background: var(--page-bg);
  }
  .canvas {
    position: relative;
    width: 1200px;
    height: 1000px;
    font-family: "Quicksand", sans-serif;
  }
  .card-shape {
    position: absolute;
    left: 0;
    top: 0;
  }
  .brand {
    position: absolute;
    left: 0;
    width: 1200px;
    top: 272px;
    display: flex;
    align-items: center;
    justify-content: center;
    gap: 18px;
  }
  .brand-dot {
    width: 58px;
    height: 58px;
    border-radius: 50%;
    background: var(--brand-mark);
  }
  .brand-name {
    font-size: 30px;
    font-weight: 500;
    letter-spacing: 3px;
    color: var(--text-soft);
    text-transform: uppercase;
  }
  .identity {
    position: absolute;
    left: 196px;
    top: 460px;
    max-width: 380px;
    color: var(--text-main);
  }
  .identity-name {
    font-size: 38px;
    font-weight: 500;
    line-height: 1;
    white-space: nowrap;
  }
  .identity-role {
    margin: 10px 0 0 9px;
    font-size: 24px;
    font-weight: 500;
    line-height: 1;
  }
  .contact {
    position: absolute;
    right: 218px;
    top: 461px;
    max-width: 380px;
    text-align: right;
    color: var(--text-main);
    font-size: 27px;
    font-weight: 400;
    line-height: 35px;
    list-style: none;
    white-space: nowrap;
  }
  .contact-phone {
    margin-top: 6px;
    font-weight: 500;
  }
</style>
</head>
<body>
<main class="canvas">
  <svg class="card-shape" width="1200" height="1000" viewBox="0 0 1200 1000" aria-hidden="true">
    <defs>
      <linearGradient id="band-fill" x1="0" y1="0" x2="0" y2="1">
        <stop offset="0" stop-color="var(--band-dark)"/>
        <stop offset="0.5" stop-color="var(--band-light)"/>
        <stop offset="1" stop-color="var(--band-dark)"/>
      </linearGradient>
    </defs>
    <path class="card-body" d="M168 176 H968 Q1008 176 1008 216 V662 H208 Q168 662 168 622 Z" fill="var(--card-base)"/>
    <polygon class="card-top-strip" points="168,176 632,176 604,189 168,189" fill="var(--card-edge)"/>
    <polygon class="card-bottom-strip" points="578,650 1008,650 1008,662 552,662" fill="var(--card-edge)"/>
    <rect class="info-band" x="168" y="438" width="840" height="152" fill="url(#band-fill)"/>
    <rect class="info-divider" x="583" y="444" width="3" height="144" fill="var(--divider)"/>
  </svg>

  <div class="brand">
    <span class="brand-dot"></span>
    <span class="brand-name">Marcus Dolven Photography</span>
  </div>

  <div class="identity">
    <h1 class="identity-name">Marcus Dolven</h1>
    <p class="identity-role">Photographer</p>
  </div>

  <ul class="contact">
    <li class="contact-email">marcus@dolven.example</li>
    <li class="contact-web">www.MarcusDolven.example</li>
    <li class="contact-phone">306 555 0142</li>
  </ul>
</main>
</body>
</html>
```